Wed site for biomedical device startup

We need a generic website for a medical device startup. I will provide examples below of websites from other companies that can serve as models for what we are looking for. The startup is for a device that can non invasively measure blood flow in the brain using light. The application is to detect the type of stroke someone is having before they get to the hospital so treatment can be started right away. This saves patients upto hours of delayed treatment. Patients will be able to recover from stroke much better and faster as a result. I have attached an AI generated illustration of what the device will ultimately look like for reference.

https://www.872vantora.com
https://quilvesta.com

Target Market(s)

Biomedical, medical device, investors of biomedical device startups

Industry/Entity Type

Biomedical

Coding

Coded - Design and coding required

Number of Pages Required

4 page

Requirements
Must have
• same section and section headings as example websites listed above
Nice to have
• similar to example websites listed above. Prefer a darker website over a lighter one. Perhaps dark blues to go with logo colors. A moving background image element at top of landing page could be cool. Something indicative of heartbeat, or neurons, or blood flow.

```html
<!DOCTYPE html>
<html lang="en">
<head>
<meta charset="utf-8">
<title>ORVELA — Smart Stroke Detection</title>
<link href="https://fonts.googleapis.com/css2?family=Nunito+Sans:wght@400;600;700&family=Poppins:wght@300;400;500;600&display=swap" rel="stylesheet">
<style>
:root{
  --bg:#0a1230;
  --bg-deep:#070d24;
  --panel:#101c45;
  --card-blue:#13285a;
  --card-violet:#24195a;
  --ink:#eef2ff;
  --ink-soft:#aab4d6;
  --violet:#7d6bff;
  --line:#26305a;
  --white:#ffffff;
  --grad:linear-gradient(90deg,#8a4cf0 0%,#5a78ee 60%,#32bdf0 100%);
}
*{margin:0;padding:0;box-sizing:border-box}
html,body{width:1200px;height:3558px;overflow:hidden;background:var(--bg)}
body{position:relative;font-family:"Poppins",sans-serif;color:var(--ink)}
.abs{position:absolute}
h1,h2,h3{font-family:"Nunito Sans",sans-serif;font-weight:400;color:var(--ink);letter-spacing:.2px}
.grad-text{background:var(--grad);-webkit-background-clip:text;background-clip:text;color:transparent;font-weight:700}
.btn{display:flex;align-items:center;justify-content:center;background:var(--grad);color:var(--white);font-size:13px;font-weight:600;letter-spacing:1.6px;border-radius:3px;text-decoration:none}

/* header */
.brand{display:flex;align-items:center;gap:10px;text-decoration:none}
.brand-dot{width:34px;height:34px;border-radius:50%;background:var(--violet)}
.brand-name{font-family:"Poppins",sans-serif;font-size:27px;font-weight:400;color:var(--ink);letter-spacing:1px}
.site-nav a{position:absolute;top:42px;font-size:14px;font-weight:500;letter-spacing:.8px;color:var(--ink);text-decoration:none}
.nav-contact{left:920px;width:110px;height:36px;top:33px !important;border:1.5px solid var(--violet);border-radius:3px;display:flex;align-items:center;justify-content:center}

/* hero */
.hero-photo{left:400px;top:0;width:800px;height:718px;
  background:radial-gradient(ellipse 55% 50% at 62% 40%,rgba(120,90,240,.55) 0%,rgba(50,120,230,.28) 45%,rgba(10,18,48,0) 80%),
  linear-gradient(90deg,var(--bg) 0%,#0e1a44 30%,#132257 100%)}
.hero-fade{left:0;top:560px;width:1200px;height:160px;background:linear-gradient(180deg,rgba(10,18,48,0) 0%,var(--bg) 100%)}
.hero-title{left:113px;top:184px;font-size:56px;line-height:66px}
.hero-copy{left:113px;top:326px;width:430px;font-size:13.5px;line-height:22px;color:var(--ink-soft);font-weight:300}

/* help */
.section-title{width:1200px;left:0;text-align:center;font-size:43px}
.help-copy{left:370px;top:754px;width:460px;text-align:center;font-size:13.5px;line-height:22px;color:var(--ink-soft);font-weight:300}
.learn-more{left:546px;top:894px;font-size:13px;font-weight:600;letter-spacing:1.4px;color:var(--violet);padding-bottom:5px;border-bottom:1.5px solid var(--violet);display:flex;align-items:center;gap:8px;text-decoration:none}
.learn-more::before{content:"";width:5px;height:5px;border-radius:50%;background:var(--violet)}

/* tech panel */
.tech-panel{left:44px;top:1009px;width:1113px;height:1224px;background:var(--panel);overflow:hidden}
.tech-glow{border-radius:50%;filter:blur(40px)}
.photo-fill{background:linear-gradient(135deg,#2a3a7a 0%,#3b3f8e 45%,#1c2a5e 100%)}
.block-title{font-size:31px;line-height:41px}
.sub-label{font-family:"Nunito Sans",sans-serif;font-weight:700;font-size:16px;color:var(--ink)}
.ticks{list-style:none}
.ticks li{display:flex;align-items:center;gap:10px;font-size:13.5px;color:var(--ink);height:34px}
.ticks svg{flex:none}
.body-copy{font-size:13.5px;line-height:22px;color:var(--ink-soft);font-weight:300}

/* cards */
.care-card{width:459px;height:448px;border-radius:10px;overflow:hidden}
.care-card.current{left:117px;top:2407px;background:var(--card-blue)}
.care-card.future{left:624px;top:2407px;background:var(--card-violet)}
.card-notch{width:120px;height:120px;border-radius:50%;background:var(--bg)}
.card-icon{width:96px;height:96px;border-radius:50%;background:var(--grad);display:flex;align-items:center;justify-content:center}
.card-title{font-size:33px;line-height:42px}
.card-inner{left:61px;top:64px}

/* newsletter */
.connect-band{left:0;top:2950px;width:1200px;height:337px;background:linear-gradient(100deg,#1796c8 0%,#3262c4 35%,#4a43b8 60%,#6e2fb4 85%,#8a2eb0 100%)}
.connect-title{left:117px;top:3030px;font-size:42px;color:var(--white)}
.connect-title b{font-weight:700}
.connect-copy{left:117px;top:3101px;width:450px;font-size:13px;line-height:21px;color:rgba(255,255,255,.78);font-weight:300}
.contact-line{left:117px;top:3163px;display:flex;gap:22px;font-size:13px;color:var(--white)}
.contact-line span{display:flex;align-items:center;gap:8px}
.band-divider{left:599px;top:3031px;width:1px;height:166px;background:rgba(255,255,255,.6)}
.join-copy{left:624px;top:3046px;width:420px;font-size:13px;line-height:21px;color:rgba(255,255,255,.88);font-weight:600}
.signup{left:624px;top:3125px;width:437px;height:51px;background:var(--white);border-radius:4px;display:flex;align-items:center;padding:3px}
.signup span{flex:1;padding-left:13px;font-size:12.5px;color:#2b2b33}
.signup .btn{width:109px;height:45px;border-radius:3px;background:linear-gradient(90deg,#6a3fd8,#2fb3e8)}

/* footer */
.footer-area{left:0;top:3287px;width:1200px;height:271px;background:var(--bg-deep)}
.footer-brand{left:0;width:1200px;top:3332px;justify-content:center}
.footer-nav a{position:absolute;top:3417px;font-size:14px;font-weight:500;letter-spacing:.8px;color:var(--ink);text-decoration:none;transform:translateX(-50%)}
.footer-rule{left:35px;top:3472px;width:1165px;height:1px;background:var(--line)}
.copyright{left:0;width:1200px;top:3508px;text-align:center;font-size:12px;letter-spacing:1px;color:#7f89ad}
</style>
</head>
<body>

<div class="abs hero-photo" role="img" aria-label="Photo of a paramedic placing a light-based sensor on a patient's forehead"></div>
<div class="abs hero-fade"></div>

<header>
  <a class="abs brand" style="left:117px;top:29px" href="#">
    <span class="brand-dot"></span><span class="brand-name">ORVELA</span>
  </a>
  <nav class="site-nav">
    <a style="left:600px" href="#">HOME</a>
    <a style="left:686px" href="#">ABOUT</a>
    <a style="left:779px" href="#">TECHNOLOGY</a>
    <a class="nav-contact" href="#">CONTACT</a>
  </nav>
</header>

<section class="hero">
  <h1 class="abs hero-title"><span class="grad-text">SMART STROKE</span><br>FLOW MONITORING</h1>
  <p class="abs hero-copy">Portable light-based technology that measures blood flow in the brain, helping responders identify stroke type before patients reach the hospital.</p>
  <a class="abs btn" style="left:113px;top:429px;width:194px;height:46px" href="#">CONNECT WITH US</a>
</section>

<section class="help">
  <h2 class="abs section-title" style="top:684px"><span class="grad-text">HOW</span> WE HELP</h2>
  <p class="abs help-copy">In a stroke, every minute counts. Treatment cannot begin until a hospital scan shows whether the stroke is caused by a clot or a bleed. By reading cerebral blood flow in the ambulance, our device lets care teams start the right treatment hours sooner.</p>
  <a class="abs learn-more" href="#">LEARN MORE</a>
</section>

<section class="abs tech-panel">
  <div class="abs tech-glow" style="left:860px;top:-40px;width:260px;height:260px;background:rgba(130,90,250,.35)"></div>
  <div class="abs tech-glow" style="left:-60px;top:780px;width:180px;height:300px;background:rgba(90,110,250,.3)"></div>

  <h2 class="abs block-title" style="left:73px;top:165px">LIFE-CHANGING<br>TECHNOLOGY FOR<br>STROKE PATIENTS</h2>
  <p class="abs sub-label" style="left:73px;top:307px">What is LUMIRA</p>
  <ul class="abs ticks" style="left:73px;top:345px">
    <li><svg width="16" height="16" viewBox="0 0 16 16"><circle cx="8" cy="8" r="7" fill="none" stroke="#8b7bff" stroke-width="1.3"/><path d="M4.8 8.2l2.2 2.1 4.2-4.4" fill="none" stroke="#8b7bff" stroke-width="1.3"/></svg>Non-invasive real-time cerebral blood flow device</li>
    <li><svg width="16" height="16" viewBox="0 0 16 16"><circle cx="8" cy="8" r="7" fill="none" stroke="#8b7bff" stroke-width="1.3"/><path d="M4.8 8.2l2.2 2.1 4.2-4.4" fill="none" stroke="#8b7bff" stroke-width="1.3"/></svg>Identifies stroke type before hospital arrival</li>
    <li><svg width="16" height="16" viewBox="0 0 16 16"><circle cx="8" cy="8" r="7" fill="none" stroke="#8b7bff" stroke-width="1.3"/><path d="M4.8 8.2l2.2 2.1 4.2-4.4" fill="none" stroke="#8b7bff" stroke-width="1.3"/></svg>Exclusive IP license from Northbridge General Hospital</li>
    <li><svg width="16" height="16" viewBox="0 0 16 16"><circle cx="8" cy="8" r="7" fill="none" stroke="#8b7bff" stroke-width="1.3"/><path d="M4.8 8.2l2.2 2.1 4.2-4.4" fill="none" stroke="#8b7bff" stroke-width="1.3"/></svg>Currently in clinical evaluation</li>
  </ul>
  <div class="abs photo-fill" style="left:558px;top:53px;width:485px;height:559px" role="img" aria-label="Photo of a patient resting while wearing a head-mounted light sensor"></div>

  <div class="abs photo-fill" style="left:73px;top:614px;width:485px;height:559px;background:linear-gradient(160deg,#1b2a62 0%,#2e3f88 45%,#3a2f80 75%,#18245a 100%)" role="img" aria-label="Photo of emergency responders caring for a patient inside an ambulance"></div>
  <h2 class="abs block-title" style="left:642px;top:766px">LUMIRA EXPLAINED</h2>
  <p class="abs body-copy" style="left:642px;top:831px;width:375px">Our probe delivers a small amount of coherent, red light through the skin.</p>
  <p class="abs body-copy" style="left:642px;top:891px;width:375px">The resulting reflection pattern has a variable intensity, called speckle, that changes from the motion of red blood cells in the field of exposure. We use a computational algorithm to resolve the relative amount of motion that directly correlates to the blood flow.</p>
  <a class="abs btn" style="left:642px;top:1032px;width:194px;height:47px" href="#">CONNECT WITH US</a>
</section>

<section class="services">
  <h2 class="abs section-title" style="top:2301px"><span class="grad-text">WHAT</span> WE DO</h2>

  <article class="abs care-card current">
    <div class="card-inner abs">
      <h3 class="card-title">CURRENT<br>STANDARD OF CARE</h3>
      <p class="sub-label" style="margin-top:16px;font-weight:600">Hospital CT Imaging</p>
      <ul class="ticks" style="margin-top:22px">
        <li><svg width="16" height="16" viewBox="0 0 16 16"><circle cx="8" cy="8" r="7" fill="none" stroke="#8b7bff" stroke-width="1.3"/><path d="M4.8 8.2l2.2 2.1 4.2-4.4" fill="none" stroke="#8b7bff" stroke-width="1.3"/></svg>Available only after hospital arrival</li>
        <li><svg width="16" height="16" viewBox="0 0 16 16"><circle cx="8" cy="8" r="7" fill="none" stroke="#8b7bff" stroke-width="1.3"/><path d="M4.8 8.2l2.2 2.1 4.2-4.4" fill="none" stroke="#8b7bff" stroke-width="1.3"/></svg>Not continuous</li>
        <li><svg width="16" height="16" viewBox="0 0 16 16"><circle cx="8" cy="8" r="7" fill="none" stroke="#8b7bff" stroke-width="1.3"/><path d="M4.8 8.2l2.2 2.1 4.2-4.4" fill="none" stroke="#8b7bff" stroke-width="1.3"/></svg>Delays treatment by up to hours</li>
        <li><svg width="16" height="16" viewBox="0 0 16 16"><circle cx="8" cy="8" r="7" fill="none" stroke="#8b7bff" stroke-width="1.3"/><path d="M4.8 8.2l2.2 2.1 4.2-4.4" fill="none" stroke="#8b7bff" stroke-width="1.3"/></svg>Large, fixed and costly equipment</li>
        <li><svg width="16" height="16" viewBox="0 0 16 16"><circle cx="8" cy="8" r="7" fill="none" stroke="#8b7bff" stroke-width="1.3"/><path d="M4.8 8.2l2.2 2.1 4.2-4.4" fill="none" stroke="#8b7bff" stroke-width="1.3"/></svg>Requires radiation exposure</li>
      </ul>
    </div>
  </article>
  <div class="abs card-notch" style="left:491px;top:2372px"></div>
  <div class="abs card-icon" style="left:503px;top:2384px">
    <svg width="50" height="50" viewBox="0 0 50 50" fill="none" stroke="#fff" stroke-width="2.4" stroke-linejoin="round" stroke-linecap="round"><path d="M25 40C12 31 8 25 8 18a8 8 0 0 1 17-4 8 8 0 0 1 17 4c0 7-4 13-17 22z"/><path d="M13 22h7l3-5 4 9 3-4h7"/></svg>
  </div>

  <article class="abs care-card future">
    <div class="card-inner abs">
      <h3 class="card-title">FUTURE<br>STANDARD OF CARE</h3>
      <p class="sub-label" style="margin-top:16px;font-weight:600">LUMIRA</p>
      <ul class="ticks" style="margin-top:22px">
        <li><svg width="16" height="16" viewBox="0 0 16 16"><circle cx="8" cy="8" r="7" fill="none" stroke="#8b7bff" stroke-width="1.3"/><path d="M4.8 8.2l2.2 2.1 4.2-4.4" fill="none" stroke="#8b7bff" stroke-width="1.3"/></svg>Works in the ambulance, on the way</li>
        <li><svg width="16" height="16" viewBox="0 0 16 16"><circle cx="8" cy="8" r="7" fill="none" stroke="#8b7bff" stroke-width="1.3"/><path d="M4.8 8.2l2.2 2.1 4.2-4.4" fill="none" stroke="#8b7bff" stroke-width="1.3"/></svg>Continuous blood flow reading</li>
        <li><svg width="16" height="16" viewBox="0 0 16 16"><circle cx="8" cy="8" r="7" fill="none" stroke="#8b7bff" stroke-width="1.3"/><path d="M4.8 8.2l2.2 2.1 4.2-4.4" fill="none" stroke="#8b7bff" stroke-width="1.3"/></svg>Lets treatment start right away</li>
        <li><svg width="16" height="16" viewBox="0 0 16 16"><circle cx="8" cy="8" r="7" fill="none" stroke="#8b7bff" stroke-width="1.3"/><path d="M4.8 8.2l2.2 2.1 4.2-4.4" fill="none" stroke="#8b7bff" stroke-width="1.3"/></svg>Compact, portable and low cost</li>
        <li><svg width="16" height="16" viewBox="0 0 16 16"><circle cx="8" cy="8" r="7" fill="none" stroke="#8b7bff" stroke-width="1.3"/><path d="M4.8 8.2l2.2 2.1 4.2-4.4" fill="none" stroke="#8b7bff" stroke-width="1.3"/></svg>Safe light, no radiation</li>
      </ul>
    </div>
  </article>
  <div class="abs card-notch" style="left:998px;top:2372px"></div>
  <div class="abs card-icon" style="left:1010px;top:2384px">
    <svg width="50" height="50" viewBox="0 0 50 50" fill="none" stroke="#fff" stroke-width="2.4" stroke-linejoin="round" stroke-linecap="round"><path d="M27 26C19 20 17 16 17 12a5 5 0 0 1 10-2 5 5 0 0 1 10 2c0 4-2 8-10 14z"/><path d="M6 38l8-7h10c2 0 2 3 0 3h-6"/><path d="M24 34l12-5c3-1 4 2 2 3L22 40H10"/></svg>
  </div>
</section>

<section class="newsletter">
  <div class="abs connect-band" role="img" aria-label="Soft blurred photo of a care team with a patient under a blue-to-purple tint"></div>
  <h2 class="abs connect-title"><b>STAY</b> CONNECTED</h2>
  <p class="abs connect-copy">Join our community to receive updates about our latest developments and research in stroke detection technology.</p>
  <div class="abs contact-line">
    <span><svg width="14" height="11" viewBox="0 0 14 11"><rect x="0.5" y="0.5" width="13" height="10" rx="1.5" fill="#fff"/><path d="M1 1.5l6 4.5 6-4.5" fill="none" stroke="#4f72df" stroke-width="1.2"/></svg>info@orvela.com</span>
    <span><svg width="13" height="13" viewBox="0 0 24 24"><path fill="#fff" d="M6.6 10.8a15 15 0 0 0 6.6 6.6l2.2-2.2a1 1 0 0 1 1-.25 11.4 11.4 0 0 0 3.6.57 1 1 0 0 1 1 1V20a1 1 0 0 1-1 1A17 17 0 0 1 3 4a1 1 0 0 1 1-1h3.5a1 1 0 0 1 1 1c0 1.25.2 2.45.57 3.6a1 1 0 0 1-.25 1z"/></svg>(415) 555-0142</span>
  </div>
  <div class="abs band-divider"></div>
  <p class="abs join-copy">Join our community to receive updates about our latest developments and research in stroke detection technology.</p>
  <form class="abs signup"><span>Email address</span><a class="btn" href="#">SUBMIT</a></form>
</section>

<footer>
  <div class="abs footer-area"></div>
  <a class="abs brand footer-brand" href="#"><span class="brand-dot" style="width:44px;height:44px"></span><span class="brand-name" style="font-size:34px">ORVELA</span></a>
  <nav class="footer-nav">
    <a style="left:380px" href="#">HOME</a>
    <a style="left:501px" href="#">ABOUT</a>
    <a style="left:650px" href="#">TECHNOLOGY</a>
    <a style="left:809px" href="#">CONTACT</a>
  </nav>
  <div class="abs footer-rule"></div>
  <p class="abs copyright">2025 ORVELA. All rights reserved.</p>
</footer>

</body>
</html>
```